Information Technology Company needs a Website...

We need a single page website for new technology company called:

MERIVALE CREST TECHNOLOGY GROUP
Based in Ojai CA.

We are offering three primary services:

- Business Solutions

- IT Services

- Software Implementation and Consulting

We want a single page design where all content scrolls down/up on one page. We're looking for the following characteristics:

- Home/Landing
- Active background with panoramic view (Will provide content)

- Business Solutions, IT Services, Software Implementation and Consulting

List of software vendors we recommend (Company logos)

- About
- History
- Our Team
- Partners

I'll upload our new logo as soon as we get the design files. I'll also send over some example website layout's that we like shortly.

Target Market(s)

Small/Medium Businesses

Industry/Entity Type

Information Technology

Number of Pages Required

1 page

Font styles to use
Other font styles liked:
• Sansation

Requirements
Must have
• Full page browser width, easy navigation and visibility. Creative design, not like every other "Technology" website template. Should be the "One Page" design where each section is below the next and the user scrolls down the page through the whole site. I like the concept of the following website in the main "Whiteboard" image:
• http://www.plinkoria-sample.com/design/4082913
• And the way this site does the active panoramic background:
• http://www.vantrelwork-sample.com/
• Something interesting and appealing to potential clients looking for Small/Medium business solutions and IT Services.
• Use uploaded Logo to establish color and theme for website.
Should not have
• Look the same as every other information technology website template.

```html
<!DOCTYPE html>
<html lang="en">
<head>
<meta charset="utf-8">
<title>Merivale Crest Technology Group</title>
<link rel="stylesheet" href="https://fonts.googleapis.com/css2?family=Lato:wght@400;700&family=Ubuntu:wght@400;500&display=swap">
<style>
:root{
  --accent:#f15a24;
  --text:#ffffff;
  --muted:#d6d6d6;
  --bg-top:#2b2b2b;
  --bg-bottom:#1c1c1c;
  --rule:#8a8a8a;
  --frame:#bcbcbc;
}
*{margin:0;padding:0;box-sizing:border-box}
html,body{width:778px;height:1200px;overflow:hidden;background:var(--bg-bottom)}
body{position:relative;font-family:"Lato",sans-serif;color:var(--text)}
.backdrop{position:absolute;inset:0;background:linear-gradient(180deg,#313131 0%,#262626 40%,#2a2a2a 70%,#1d1d1d 100%)}
.abs{position:absolute}
.header{position:absolute;left:0;top:0;width:778px;height:77px;background:rgba(30,30,30,.55);border-bottom:2px solid #6d6d6d}
.logo{left:64px;top:22px;font-family:"Ubuntu",sans-serif;font-weight:500;color:#9a9a9a;line-height:1}
.logo .name{font-size:17px;letter-spacing:.5px;display:block}
.logo .sub{font-size:8px;letter-spacing:1.6px;display:block;margin-top:4px}
.contact{top:10px;font-size:10.5px;display:flex;align-items:center;gap:6px}
.contact svg{fill:var(--accent)}
.nav{top:47px;left:258px;display:flex;font-size:9px;font-family:"Ubuntu",sans-serif}
.nav a{color:var(--text);text-decoration:none;padding:0 14px;border-left:1px solid #6a6a6a;line-height:11px}
.nav a:first-child{border-left:none;color:var(--accent);position:relative}
.nav a:first-child::after{content:"";position:absolute;left:10px;right:10px;bottom:-7px;height:2px;background:var(--accent)}
.mark{height:2px;width:116px;background:#a8a8a8;border-radius:1px}
.heading{font-family:"Ubuntu",sans-serif;font-weight:500;font-size:19px;white-space:nowrap}
.heading span{color:var(--accent)}
.center{transform:translateX(-50%)}
.intro{left:74px;top:155px;width:630px;text-align:center;font-size:8.3px;line-height:15.8px;color:var(--muted)}
.rule{left:64px;width:650px;border-top:2px dotted var(--rule)}
.history-text{left:66px;top:320px;width:376px;font-size:8.3px;line-height:14.2px;color:var(--muted)}
.photo{left:475px;top:284px;width:238px;height:155px;border:3px solid var(--frame);background:linear-gradient(135deg,#e9eef2,#b8c2cc 55%,#5b6068)}
.service{width:200px;text-align:center}
.service .icon{width:68px;height:62px;border:1.5px solid var(--accent);margin:0 auto;display:flex;align-items:center;justify-content:center}
.service h3{font-family:"Ubuntu",sans-serif;font-weight:500;font-size:13px;margin-top:12px}
.service p{font-size:8.3px;line-height:12.6px;color:var(--muted);margin-top:4px}
.member{width:140px;text-align:center}
.member .portrait{width:113px;height:113px;border-radius:50%;border:4px solid var(--accent);margin:0 auto;background:radial-gradient(circle at 50% 40%,#f4f4f4,#c9c9c9 70%,#9a9a9a)}
.member h4{font-family:"Ubuntu",sans-serif;font-weight:500;font-size:10.5px;margin-top:22px}
.member p{font-size:8.5px;color:var(--muted);margin-top:4px}
.partners{left:64px;top:1060px;display:flex;gap:17px}
.badge{width:116px;height:61px;border:1.5px solid #cfcfcf;display:flex;align-items:center;justify-content:center}
.badge i{display:block;width:60px;height:22px;background:#8f8f8f;border-radius:3px}
.footer-text{left:64px;top:1173px;font-size:9.5px;color:var(--muted)}
.social{left:627px;top:1169px;display:flex;gap:3px}
.social i{display:block;width:19px;height:19px;border-radius:50%;background:var(--accent)}
</style>
</head>
<body>
<div class="backdrop" role="img" aria-label="Dark aerial panorama of a city skyline at dusk"></div>

<header class="header">
  <div class="abs logo"><span class="name">Merivale Crest</span><span class="sub">TECHNOLOGY GROUP</span></div>
  <div class="abs contact" style="left:455px">
    <svg width="10" height="10" viewBox="0 0 24 24"><path d="M6.6 10.8a15 15 0 0 0 6.6 6.6l2.2-2.2a1 1 0 0 1 1-.25 11.4 11.4 0 0 0 3.6.6 1 1 0 0 1 1 1V20a1 1 0 0 1-1 1A17 17 0 0 1 3 4a1 1 0 0 1 1-1h3.5a1 1 0 0 1 1 1c0 1.25.2 2.45.6 3.6a1 1 0 0 1-.25 1z"/></svg>
    555-014-2286
  </div>
  <div class="abs contact" style="left:558px">
    <svg width="11" height="9" viewBox="0 0 24 18"><path d="M0 0h24v18H0z M2 2l10 8 10-8" /></svg>
    merivalecrestgroup.com
  </div>
  <nav class="abs nav">
    <a href="#">Home</a><a href="#">About</a><a href="#">Services</a><a href="#">History</a><a href="#">Our Team</a><a href="#">Partners</a><a href="#">Contact Us</a>
  </nav>
</header>

<section class="about">
  <div class="abs mark" style="left:331px;top:113px"></div>
  <h2 class="abs heading center" style="left:389px;top:122px">ABOUT <span>US</span></h2>
  <p class="abs intro">Lorem ipsum dolor sit amet, consectetuer adipiscing elit, sed diam nonummy nibh euismod tincidunt ut laoreet dolore magna aliquam erat volutpat. Ut wisi enim ad minim veniam, quis nostrud exerci tation ullamcorper suscipit lobortis nisl ut aliquip ex ea commodo consequat. Duis autem vel eum iriure dolor in hendrerit in vulputate velit esse molestie consequat, vel illum dolore eu feugiat nulla facilisis at vero eros et accumsan et iusto odio dignissim qui blandit praesent luptatum zzril delenit augue duis dolore te feugait nulla facilisi.</p>
</section>
<div class="abs rule" style="top:237px"></div>

<section class="history">
  <div class="abs mark" style="left:64px;top:278px"></div>
  <h2 class="abs heading" style="left:76px;top:287px">Our <span>History</span></h2>
  <p class="abs history-text">Sed ut perspiciatis unde omnis iste natus error sit voluptatem accusantium doloremque laudantium, totam rem aperiam, eaque ipsa quae ab illo inventore veritatis et quasi architecto beatae vitae dicta sunt explicabo. Nemo enim ipsam voluptatem quia voluptas sit aspernatur aut odit aut fugit, sed quia consequuntur magni dolores eos qui ratione voluptatem sequi nesciunt. Neque porro quisquam est, qui dolorem ipsum quia dolor sit amet, consectetur, adipisci velit, sed quia non numquam eius modi tempora incidunt ut labore et dolore magnam aliquam quaerat voluptatem. Ut enim ad minima veniam, quis nostrum exercitationem ullam corporis suscipit laboriosam, nisi ut aliquid ex ea commodi consequatur.</p>
  <div class="abs photo" role="img" aria-label="Two business colleagues reviewing work on a laptop in a bright office"></div>
</section>
<div class="abs rule" style="top:467px"></div>

<section class="services">
  <div class="abs mark" style="left:331px;top:506px"></div>
  <h2 class="abs heading center" style="left:389px;top:517px">Our <span>Services</span></h2>
  <div class="abs service" style="left:63px;top:553px">
    <div class="icon"><svg width="34" height="34" viewBox="0 0 34 34" fill="#fff"><circle cx="12" cy="12" r="5"/><path d="M3 31c0-7 4-11 9-11s9 4 9 11z"/><rect x="21" y="3" width="10" height="14" rx="1" fill="none" stroke="#fff" stroke-width="1.6"/><circle cx="26" cy="8" r="2"/><circle cx="26" cy="13" r="1.5"/></svg></div>
    <h3>Business Solution</h3>
    <p>Lorem ipsum dolor sit amet, consectetur incididunt adipiscing elit, sed do eiusmod tempor labore incididunt ut labore et</p>
  </div>
  <div class="abs service" style="left:288px;top:553px">
    <div class="icon"><svg width="36" height="34" viewBox="0 0 36 34" fill="none" stroke="#fff" stroke-width="2"><rect x="3" y="3" width="24" height="17" rx="1"/><path d="M11 26h10M15 20v6"/><circle cx="27" cy="25" r="5" fill="#fff"/><circle cx="27" cy="25" r="1.8" stroke="#333"/></svg></div>
    <h3>IT Services</h3>
    <p>Lorem ipsum dolor sit amet, consectetur incididunt adipiscing elit, sed do eiusmod tempor labore incididunt ut labore et</p>
  </div>
  <div class="abs service" style="left:514px;top:553px">
    <div class="icon"><svg width="38" height="38" viewBox="0 0 38 38" fill="none" stroke="#fff" stroke-width="2.4"><path d="M7 19a12 12 0 0 1 20-9"/><path d="M31 19a12 12 0 0 1-20 9"/><path d="M27 4v6h-6M11 34v-6h6"/><circle cx="19" cy="19" r="5" fill="#fff" stroke="none"/><circle cx="19" cy="19" r="2" fill="#333" stroke="none"/></svg></div>
    <h3>Software implimentation</h3>
    <p>Lorem ipsum dolor sit amet, consectetur incididunt adipiscing elit, sed do eiusmod tempor labore incididunt ut labore et</p>
  </div>
</section>
<div class="abs rule" style="top:708px"></div>

<section class="team">
  <div class="abs mark" style="left:331px;top:746px"></div>
  <h2 class="abs heading center" style="left:389px;top:756px">Our <span>Team</span></h2>
  <div class="abs member" style="left:70px;top:789px">
    <div class="portrait" role="img" aria-label="Portrait of team member Evan Marlowe"></div>
    <h4>Evan Marlowe</h4><p>Lorem Ipsum</p>
  </div>
  <div class="abs member" style="left:230px;top:789px">
    <div class="portrait" role="img" aria-label="Portrait of team member Devin Castell"></div>
    <h4>Devin Castell</h4><p>Lorem Ipsum</p>
  </div>
  <div class="abs member" style="left:403px;top:789px">
    <div class="portrait" role="img" aria-label="Portrait of team member Marco Ellery"></div>
    <h4>Marco Ellery</h4><p>Lorem Ipsum</p>
  </div>
  <div class="abs member" style="left:568px;top:789px">
    <div class="portrait" role="img" aria-label="Portrait of team member Graham Holloway"></div>
    <h4>Graham Holloway</h4><p>Lorem Ipsum</p>
  </div>
</section>
<div class="abs rule" style="top:974px"></div>

<section class="partner-list">
  <div class="abs mark" style="left:331px;top:1014px"></div>
  <h2 class="abs heading center" style="left:389px;top:1024px">Our <span>Partners</span></h2>
  <div class="abs partners">
    <div class="badge"><i></i></div>
    <div class="badge"><i></i></div>
    <div class="badge"><i></i></div>
    <div class="badge"><i></i></div>
    <div class="badge"><i></i></div>
  </div>
</section>
<div class="abs rule" style="top:1156px"></div>

<footer>
  <p class="abs footer-text">© 2016 &nbsp;merivalecrestgroup.com | All Rights Reserved</p>
  <div class="abs social"><i></i><i></i><i></i><i></i></div>
</footer>
</body>
</html>
```